依頼詳細
PCとスマホデザインの両方納品をいただきますが、
まずはデザインイメージが確認しやすいPCページのみの提案をお願いします。
スマホページは当選者に納品時にお願いしたいと思います。
スマホサイズは横幅750pxのサイズで作成してください。

レスポンシブウェブデザインを意識したデザインでお願いします。

デザインに関しては、添付してあるデザインレイアウト設計シートを基にお願いします。
参考サイトのURLはデザインレイアウト設計シートに記載してあります。

画像データについては、フリー素材から流用してイメージ画像に当て込んでください。

足りない場合は、一旦他のサイトの写真をサンプルとして入れてください。
また、購入が必要な写真などを利用した場合、価格とサイト名を教えてください。
ページ数
1ページ
希望イメージ
シンプル 複雑
単色 カラフル
暗い 明るい
日常 高級
遊び心 厳粛
未来的 伝統的
女性的 男性的
納品ファイル
• イラストレーター形式 (.ai)
• フォトショップ形式 (.psd)
• PNG形式 (.png)
補足説明
上記のいずれか1つ(アウトラインありとなしの2つ)と高解像度JPGを納品お願いします。

クライアント様より選定いただきました。
一番イメージに近いものでした

ご提案ありがとうございました。
また機会がありましたら是非お願いします。

```html
<!DOCTYPE html>
<html lang="ja">
<head>
<meta charset="utf-8">
<title>株式会社青葉製作所</title>
<link href="https://fonts.googleapis.com/css2?family=Noto+Serif+JP:wght@500;700&family=Noto+Sans+JP:wght@400;500;700&family=Poppins:wght@400;500&display=swap" rel="stylesheet">
<style>
:root{
  --green:#2f9a78;
  --green-dark:#237f62;
  --ink:#333;
  --muted:#777;
  --line:#e3e3e3;
  --faint:#eef5f1;
  --bg:#fff;
  --soft:#f6f6f6;
  --red:#c9483c;
  --sans:"Noto Sans JP",sans-serif;
  --serif:"Noto Serif JP",serif;
  --latin:"Poppins",sans-serif;
}
*{box-sizing:border-box;margin:0;padding:0}
html,body{width:1200px;height:3276px;overflow:hidden;background:var(--bg);color:var(--ink);font-family:var(--sans)}
.page{position:relative;width:1200px;height:3276px;overflow:hidden}
.abs{position:absolute}
/* header */
.site-header{position:absolute;top:0;left:0;width:1200px;height:70px;background:rgba(255,255,255,.96);z-index:5;display:flex;align-items:center;padding:0 32px}
.brand{display:flex;align-items:center;gap:10px;font-family:var(--serif);font-weight:700;font-size:20px;color:var(--ink);white-space:nowrap}
.brand-mark{width:22px;height:22px;background:var(--green)}
.global-nav{margin-left:auto;display:flex;align-items:center;gap:26px;font-size:12px}
.btn{display:inline-flex;align-items:center;justify-content:center;background:var(--green);color:#fff;font-size:12px;letter-spacing:.08em;white-space:nowrap}
.global-nav .btn{width:132px;height:34px}
/* hero */
.hero-photo{left:0;top:0;width:1200px;height:720px;background:linear-gradient(100deg,#b9b6ad 0%,#d7d4cc 35%,#cfd0cb 60%,#8f9288 100%)}
.hero-catch{left:572px;top:94px;width:80px;height:330px;background:#fff;display:flex;justify-content:center;padding-top:22px}
.hero-catch span{writing-mode:vertical-rl;font-family:var(--serif);font-weight:700;font-size:50px;letter-spacing:.12em;color:#222}
.hero-catch::after{content:"";position:absolute;left:-6px;top:0;width:4px;height:330px;background:var(--green)}
.hero-sub{left:502px;top:96px;writing-mode:vertical-rl;font-family:var(--serif);font-size:17px;line-height:34px;letter-spacing:.3em;color:#333;background:rgba(255,255,255,.8);padding:10px 4px;height:260px}
/* headings */
.sec-title{text-align:center;font-family:var(--serif);font-weight:500;font-size:24px}
.sec-en{text-align:center;font-family:var(--latin);font-size:11px;color:var(--green);margin-top:6px}
.ghost{font-family:var(--latin);font-weight:500;color:var(--faint);line-height:1;white-space:nowrap}
/* about */
.about-head{left:0;top:820px;width:1200px;z-index:2}
.about-photo{left:0;top:905px;width:600px;height:345px;background:linear-gradient(135deg,#6b5c4c,#b4967a 45%,#8d7a68)}
.about-body{left:688px;top:1015px;width:330px}
.about-body h3{font-family:var(--serif);font-weight:500;font-size:19px;line-height:1.7;border-left:3px solid var(--green);padding-left:14px}
.about-body p{font-size:12px;line-height:2;color:var(--muted);margin-top:22px}
.about-body .btn{width:120px;height:36px;margin-top:30px}
/* cards */
.card{width:395px;height:290px;color:#fff}
.card-photo{position:absolute;inset:0}
.card-label{position:absolute;left:22px;top:22px}
.card-label b{display:block;font-size:19px;font-weight:700}
.card-label i{font-style:normal;font-family:var(--latin);font-size:10px}
/* news */
.news-head{left:195px;top:2030px}
.news-head h2{font-family:var(--serif);font-weight:500;font-size:22px}
.news-head .en{font-family:var(--latin);font-size:11px;color:var(--green);margin-top:4px}
.news-head .btn{width:150px;height:36px;margin-top:42px}
.news-list{left:410px;top:2050px;width:590px;list-style:none}
.news-list li{display:flex;gap:36px;font-size:12px;height:58px;align-items:center;border-bottom:1px solid var(--line)}
.news-list time{font-family:var(--latin);color:var(--muted);width:80px}
/* shop band */
.shop-band{left:0;top:2405px;width:1200px;height:285px;background:var(--green)}
.shop-card{width:395px;height:92px;background:#fff;display:flex;flex-direction:column;align-items:center;justify-content:center;gap:6px}
.shop-card .name{display:flex;align-items:center;gap:8px;font-family:var(--serif);font-weight:700;font-size:20px;white-space:nowrap}
.shop-card .name i{width:22px;height:22px;background:var(--green)}
.shop-card .tag{font-size:11px;color:#fff;background:var(--green);padding:3px 18px}
.shop-card .tag.alt{background:var(--red)}
/* contact */
.contact-box{left:340px;top:2745px;width:520px;height:210px;background:var(--soft);display:flex;align-items:center;padding:0 44px}
.contact-l{width:200px}
.contact-l h2{font-family:var(--serif);font-weight:500;font-size:20px}
.contact-l .en{font-family:var(--latin);font-size:10px;color:var(--green);margin:3px 0 16px}
.contact-l p{font-size:11px;line-height:1.9;color:var(--muted)}
.contact-r{margin-left:auto;width:220px}
.tel{display:flex;align-items:center;gap:6px;font-family:var(--latin);font-size:24px;font-weight:500;white-space:nowrap}
.hours{font-size:10px;color:var(--muted);margin:4px 0 14px 26px}
.contact-r .btn{width:170px;height:36px}
/* footer */
.site-footer{left:0;top:3010px;width:1200px;height:266px;border-top:1px solid var(--line)}
.site-footer .brand{position:absolute;left:195px;top:50px}
.footer-addr{position:absolute;left:195px;top:100px;font-size:10px;line-height:2;color:var(--muted)}
.footer-nav{position:absolute;left:650px;top:52px;display:flex;gap:22px;font-size:11px}
.footer-nav.sub{top:80px;color:var(--muted)}
.copy{position:absolute;left:650px;top:188px;font-family:var(--latin);font-size:10px;color:var(--muted)}
</style>
</head>
<body>
<div class="page">

  <div class="abs hero-photo" role="img" aria-label="倉庫の棚の前に立つ作業着姿のスタッフの写真"></div>
  <header class="site-header">
    <div class="brand"><span class="brand-mark"></span>株式会社青葉製作所</div>
    <nav class="global-nav">
      <span>事業内容</span><span>製品情報</span><span>採用情報</span><span>会社案内</span>
      <span class="btn">お問い合わせ</span>
    </nav>
  </header>
  <p class="abs hero-sub">わが社に関わる<br>すべての人に笑顔を</p>
  <div class="abs hero-catch"><span>人間尊重</span></div>

  <section>
    <div class="abs ghost" style="left:880px;top:900px;font-size:120px">About</div>
    <div class="abs about-head">
      <h2 class="sec-title">青葉製作所について</h2>
      <p class="sec-en">About</p>
    </div>
    <div class="abs about-photo" role="img" aria-label="段ボールが積まれた倉庫ラックの写真"></div>
    <div class="abs about-body">
      <h3>「物流と倉庫の収納・保管」の<br>効率化・安全化を提案します</h3>
      <p>当社は物流機器の設計から製造、施工までを一貫して手がけています。現場の声に耳を傾け、働く人が安心して作業できる環境づくりを支えます。</p>
      <span class="btn">会社案内</span>
    </div>
  </section>

  <section>
    <div class="abs ghost" style="left:-10px;top:1355px;font-size:140px">Product</div>
    <div class="abs ghost" style="left:610px;top:1780px;font-size:140px">Case stu</div>
    <div class="abs card" style="left:195px;top:1530px">
      <div class="card-photo" role="img" aria-label="倉庫に積まれた製品の写真" style="background:linear-gradient(135deg,#5b4c3e,#9c8266 55%,#6e5d4c)"></div>
      <div class="card-label"><b>製品情報</b><i>Product</i></div>
    </div>
    <div class="abs card" style="left:605px;top:1530px">
      <div class="card-photo" role="img" aria-label="導入企業の担当者の写真" style="background:linear-gradient(135deg,#4a5560,#8c96a0 55%,#5e6872)"></div>
      <div class="card-label"><b>導入事例</b><i>Case studies</i></div>
    </div>
  </section>

  <section>
    <div class="abs news-head">
      <h2>お知らせ</h2>
      <p class="en">News</p>
      <span class="btn">一覧を見る</span>
    </div>
    <ul class="abs news-list">
      <li><time>2021.06.07</time><span>倉庫向け新型ラックシリーズの販売を開始しました</span></li>
      <li><time>2021.05.20</time><span>夏季休業期間のお知らせ</span></li>
      <li><time>2021.04.15</time><span>ウェブサイトをリニューアルしました</span></li>
      <li><time>2021.03.26</time><span>物流展示会への出展が決定しました</span></li>
      <li><time>2021.03.02</time><span>導入事例に新しい記事を追加しました</span></li>
    </ul>
  </section>

  <section class="abs shop-band">
    <div class="abs shop-card" style="left:195px;top:95px">
      <div class="name"><i></i>青葉製作所 ONLINE SHOP</div>
      <span class="tag">青葉製作所 公式ショップ</span>
    </div>
    <div class="abs shop-card" style="left:605px;top:95px">
      <div class="name">モールショップ</div>
      <span class="tag alt">モール店でもお買い求めいただけます</span>
    </div>
  </section>

  <section class="abs contact-box">
    <div class="contact-l">
      <h2>お問い合わせ</h2>
      <p class="en">Contact</p>
      <p>製品に関するご相談やお見積りは<br>お気軽にお問い合わせください</p>
    </div>
    <div class="contact-r">
      <div class="tel">
        <svg width="20" height="20" viewBox="0 0 24 24"><path fill="#333" d="M6.6 10.8a15 15 0 0 0 6.6 6.6l2.2-2.2c.3-.3.7-.4 1-.2 1.1.4 2.3.6 3.6.6.6 0 1 .4 1 1V20c0 .6-.4 1-1 1A17 17 0 0 1 3 4c0-.6.4-1 1-1h3.5c.6 0 1 .4 1 1 0 1.3.2 2.5.6 3.6.1.3 0 .7-.2 1z"/></svg>
        <span>0120-000-000</span>
      </div>
      <p class="hours">受付時間 平日 9:00〜17:00</p>
      <span class="btn">お問い合わせ</span>
    </div>
  </section>

  <footer class="abs site-footer">
    <div class="brand"><span class="brand-mark"></span>株式会社青葉製作所</div>
    <p class="footer-addr">〒000-0000 青葉市中央町1丁目2番3号<br>TEL 0120-000-000　FAX 0120-000-001</p>
    <nav class="footer-nav"><span>事業内容</span><span>製品情報</span><span>採用情報</span><span>会社案内</span><span>お問い合わせ</span></nav>
    <nav class="footer-nav sub"><span>個人情報保護方針</span><span>サイトマップ</span></nav>
    <p class="copy">Copyright © 2021 Aoba Seisakusho Co., Ltd. All Rights Reserved.</p>
  </footer>

</div>
</body>
</html>
```